Sponsorenmappe für die Lindenhof Jugend Bewegungs Institut
Zielgruppe
Die Lindenhof Jugend Bewegungs Institut (LJBI) bietet Schulen und Vereinen vielfältige Sport-, Bewegungs- und Ernährungsangebote.
Mit der Lindenhof Jugend Kick Institut (LJKI) und der Jugend Kick Institut (JKI) hat die LJBI-GmbH für den Fußballbereich zwei eigene Marken.
Das ganzheitliche LJBI-Konzept fördert ein sinnvolles Zusammenspiel von Schule, Sport und Persönlichkeitsentwicklung.
Das Design der Sponsorenmappe sollte natürlich in erster Linie den (vorallem mittelständischen) potentiellen Sponsoren gefallen und diese ansprechen. Hier sollte das Design klar und strukturiert sein, jedoch kleine Einflüsse der kinderaffinenen Marken besitzen.
Aufgabenstellung
Anbei haben wir schon einmal eine "Sponsorenmappe" in Word entworfen. Hierbei handelt es sich nur um einen kleinen Vorschlag wie es vielleicht aussehen könnte!
Die Textbausteine sollen jedoch verwendet werden.
Format: Din A4 - Druckdatenblatt von Papierwelle liegt bei.
Vorder- und Rückseite der Broschüre sind schon angefertig! Diese müssen noch noch angefügt werden. Tendenziell sollte die Broschüre dieses Design aufgreifen. Auch die erste Klappseite (Auf dem Druckdatenblatt als "E" gekennzeichnet - bei "D") ist schon designt. Hierbei handelt es sich um das Organigramm der LJBI (siehe Anhang). Überschrift muss jedoch noch in der jeweiligen Schriftart eingefügt werden.
Anbei finden Sie eine Win-Rar-Datei mit Logos und Bildern, die Ihnen zur Verwendung stehen.
Zudem unsere Broschüre für weitere Infos
Dem Rest geben wir küntlerische Freiheit.

```html
<!DOCTYPE html>
<html lang="de">
<head>
<meta charset="utf-8">
<title>Sponsorenmappe LJBI</title>
<link href="https://fonts.googleapis.com/css2?family=Encode+Sans+Condensed:wght@400;500;600;700&display=swap" rel="stylesheet">
<style>
:root{
  --blue:#1e9be0;
  --blue-text:#1a8fd8;
  --blue-light:#d4ebfa;
  --white:#ffffff;
  --ink:#1d1d1b;
  --navy:#2e3192;
  --magenta:#cc1a8c;
  --red:#d7191c;
  --orange:#ef8a1e;
  --yellow:#f4e525;
  --green:#3aaa35;
}
*{margin:0;padding:0;box-sizing:border-box}
html,body{width:1200px;height:663px;overflow:hidden;background:var(--blue)}
body{font-family:"Encode Sans Condensed",sans-serif;color:var(--ink)}
.folder{position:relative;width:1200px;height:663px;background:var(--blue)}
.fold{position:absolute;top:0;height:552px;border-left:1px dashed rgba(255,255,255,.8)}
.abs{position:absolute}
.card{position:absolute;background:var(--white)}
.panel-title{position:absolute;color:var(--white);font-size:16px;font-weight:400}
.photo{position:absolute;border:3px solid var(--white);box-shadow:1px 2px 4px rgba(0,0,0,.35)}
.head{color:var(--blue-text);font-weight:600;text-transform:uppercase}
ul.dots{list-style:none}
ul.dots li::before{content:"• "}
.bubble{position:absolute;width:36px;height:36px;border-radius:50%;background:var(--blue-light);color:var(--blue-text);font-size:6px;line-height:8px;text-align:center;display:flex;flex-direction:column;justify-content:center}
.brand{position:absolute;font-weight:700;color:var(--ink);white-space:nowrap;line-height:1}

/* left panel */
.logo-card{left:32px;top:40px;width:330px;height:54px;display:flex;align-items:center;justify-content:center}
.logo-name{font-weight:700;font-size:12.5px;line-height:12.5px;color:var(--ink);text-transform:uppercase}
.quote{left:40px;top:108px;width:315px;text-align:center;color:var(--white);font-size:10.5px;line-height:12.8px;font-weight:500}
.quote small{display:block;font-size:5px;line-height:9px;font-weight:400}
.badge{position:absolute;top:185px;width:65px;height:63px;background:var(--white);clip-path:polygon(0 0,100% 0,100% 62%,50% 100%,0 62%);color:var(--blue-text);font-size:13px;font-weight:500;text-align:center;padding-top:13px}
.general{left:104px;top:185px;width:190px;color:var(--white)}
.general h3{font-size:10px;font-weight:600;margin-left:8px}
.general .cols{display:flex;gap:8px;font-size:6.6px;line-height:9.4px;margin-left:8px}
.general .src{font-size:4.5px;margin-top:3px}
.offer{left:32px;top:263px;width:330px;height:90px;padding:6px 9px}
.offer h2{text-align:center;font-size:10.5px;line-height:14px;margin-bottom:4px}
.offer li{font-size:6.6px;line-height:9.4px;text-indent:-5px;padding-left:5px}
.team{left:32px;top:369px;width:330px;height:139px;padding:8px 10px;display:flex;gap:12px}
.team .col{flex:1;font-size:6.6px;line-height:9.4px;text-align:left;hyphens:auto}
.team .head{font-size:10px;line-height:9.4px;margin-right:2px}
.team p+p{margin-top:4px}

/* middle panel */
.camps{left:432px;top:69px;width:337px;height:145px}
.reisen{left:432px;top:223px;width:337px;height:144px}
.schule{left:432px;top:380px;width:337px;height:128px}
.block-h{font-size:11px}
.txt{font-size:6.6px;line-height:9.2px}
.b{font-weight:600}

/* right panel */
.rule{position:absolute;left:838px;width:330px;height:1.5px;background:rgba(255,255,255,.75)}
.pyr-label{position:absolute;left:1044px;color:var(--white);font-size:12.5px;font-weight:500}
.tab{position:absolute;width:103px;height:25px;background:var(--blue-light);color:var(--blue-text);font-size:11px;font-weight:500;display:flex;align-items:center;justify-content:flex-end;padding-right:12px;text-transform:uppercase;line-height:9px;text-align:center}
.tab::before{content:"";position:absolute;left:0;top:0;width:28px;height:25px;background:var(--white);clip-path:polygon(0 0,55% 0,100% 50%,55% 100%,0 100%)}
.csr{position:absolute;left:969px;top:277px;width:62px;height:62px;border-radius:50%;background:var(--blue-light);border:3px solid var(--white);color:var(--blue-text);font-size:11px;display:flex;align-items:center;justify-content:center}
.media{position:absolute;top:418px;width:76px;height:90px;background:var(--white);text-align:center;padding-top:35px}
.media h4{font-size:8.4px;font-weight:600;margin-bottom:2px}
.media p{font-size:6.6px;line-height:9.4px}
.media-icon{position:absolute;top:-9px;left:19px;width:38px;height:36px}
</style>
</head>
<body>
<div class="folder">

  <svg class="abs" style="left:0;top:0" width="1200" height="663" aria-hidden="true">
    <g fill="none" stroke="rgba(255,255,255,.8)" stroke-width="1" stroke-dasharray="3 2">
      <line x1="0" y1="552" x2="404" y2="552"/>
      <line x1="801" y1="552" x2="1200" y2="552"/>
      <line x1="404" y1="557" x2="801" y2="557"/>
      <polyline points="404,552 404,621 426,663"/>
      <polyline points="801,552 801,621 779,663"/>
    </g>
  </svg>
  <div class="fold" style="left:399px"></div>
  <div class="fold" style="left:403px"></div>
  <div class="fold" style="left:801px"></div>
  <div class="fold" style="left:805px"></div>

  <!-- LEFT PANEL -->
  <div class="card logo-card">
    <span class="logo-name">Lindenhof Jugend<br>Bewegungs Institut</span>
  </div>

  <p class="abs quote">„Kinder sollten mehr spielen, als viele Kinder es heutzutage tun.<br>Denn wenn man genügend spielt, solange man klein ist,<br>dann trägt man Schätze mit sich herum, aus denen man später<br>sein ganzes Leben lang schöpfen kann.“
    <small>Ingrid Solberg (1907 – 2002), schwedische Schriftstellerin</small></p>

  <div class="badge" style="left:33px">Spaß</div>
  <div class="badge" style="left:297px;font-size:12px">Bewegung</div>
  <div class="abs general">
    <h3>GENERELL GILT:</h3>
    <div class="cols">
      <p>• Kinder bewegen sich<br>&nbsp;&nbsp;weniger und treiben<br>&nbsp;&nbsp;immer seltener Sport.</p>
      <p>• 40 – 60 % der Kinder<br>&nbsp;&nbsp;haben Haltungsschwächen<br>&nbsp;&nbsp;oder Haltungsschäden.</p>
    </div>
    <p class="src">FIT-Studie (Fitness in Teens) der Hochschule für Sport Nordstadt</p>
  </div>

  <div class="card offer">
    <h2 class="head">Die LJBI bietet vielfältige Sport-, Bewegungs-<br>und Ernährungsangebote</h2>
    <ul class="dots">
      <li>Das ganzheitliche LJBI-Konzept fördert ein sinnvolles Zusammenspiel von Schule, Sport und Persönlichkeitsentwicklung.</li>
      <li>Spaß und Freude sollen Kinder und Jugendliche langfristig für Sport und Bewegung motivieren.</li>
      <li>Dabei Eltern entlasten, Kinder fördern, zahlreiche Sport- und Bewegungsangebote schaffen, Gesundheitsschäden vorbeugen und das soziale Verhalten und den Teamgeist der Kinder stärken.</li>
    </ul>
  </div>

  <div class="card team">
    <div class="col">
      <p><span class="head">Team |</span> Die qualifizierten, haupt- und nebenberuflichen Mitarbeiter in den verschiedenen Bereichen der LJBI haben langjährige Erfahrung im Kinder- und Jugendsport.</p>
      <p>Alle Übungsleiter und Lehrkräfte im Bereich unserer Sportangebote verfügen mindestens über ein: Grundstudium in einem pädagogischen, sozial- oder sportwissenschaftlichen Studiengang, haben eine spezifische Ausbildung oder Übungsleiterlizenz.</p>
    </div>
    <div class="col">
      <p><span class="head">Philosophie |</span> <span class="b">„Bei sämtlichen Angeboten der LJBI steht stets der Spaß im Vordergrund.“</span></p>
      <p><span class="b">DENN:</span> Wer mit Freude lernt, lernt schneller und nachhaltiger! Neben der sportlichen Ausbildung sollen die Kinder lernen, sich in einer Gruppe zu bewegen, soziale Kontakte zu knüpfen sowie Werten wie Fair Play, Disziplin und Gesundheitsbewusstsein mehr Bedeutung zuzuordnen.</p>
      <p><span class="b">Unser Anspruch:</span> hohe Qualität aller angebotenen Leistungen – optimale Beratung, Organisation und Betreuung – gute Zusammenarbeit mit den Kindern, Eltern und Kooperationspartnern.</p>
    </div>
  </div>

  <!-- MIDDLE PANEL -->
  <h1 class="panel-title" style="left:436px;top:42px">Kompetenz und Angebote</h1>

  <div class="card camps"></div>
  <div class="photo" role="img" aria-label="Foto: jubelnde Kinder in grünen Trikots auf dem Fußballplatz" style="left:422px;top:66px;width:112px;height:80px;transform:rotate(-2deg);background:linear-gradient(160deg,#5a7f3a,#8fc15a 55%,#3f6a28)"></div>
  <div class="photo" role="img" aria-label="Foto: Taktiktafel mit Spielzügen" style="left:432px;top:140px;width:98px;height:68px;transform:rotate(5deg);background:linear-gradient(150deg,#2b2b2b,#4a4a4a 60%,#1c1c1c)"></div>
  <div class="abs" style="left:544px;top:76px;width:130px">
    <h3 class="head block-h">Camps &amp; Spezialtraining</h3>
    <ul class="dots txt" style="margin-top:2px">
      <li>Für Mädchen und Jungen</li>
      <li>Von 5 bis 17 Jahren<br><span style="font-size:5px">&nbsp;&nbsp;(verschiedene Altersgruppen)</span></li>
      <li>2-bis 5-Tage-Camps.</li>
    </ul>
    <p class="txt" style="margin-top:3px"><span class="b">Camps pro Jahr 2015:</span> 15 – 20<br><span class="b">Tendenz 2016:</span> &nbsp;&nbsp;&nbsp;&nbsp;&nbsp;&nbsp;&nbsp;&nbsp;&nbsp;30 – 40</p>
    <p class="txt b" style="margin-top:2px">KINDER IM SCHNITT:</p>
    <p class="txt"><span class="b">Pro Camp 2015:</span> &nbsp;&nbsp;&nbsp;&nbsp;&nbsp;&nbsp;&nbsp;30 – 40<br><span class="b">Tendenz 2016:</span> &nbsp;&nbsp;&nbsp;&nbsp;&nbsp;&nbsp;&nbsp;40 – 50</p>
    <p class="txt b" style="margin-top:2px">Regionale Wahrnehmung<br>eines Camps:</p>
  </div>
  <div class="brand" style="left:688px;top:106px;font-size:16px">JKI</div>
  <div class="brand" style="left:664px;top:148px;font-size:10px">bewegt-plus.de</div>
  <div class="brand" style="left:731px;top:151px;font-size:8px">Motiva</div>
  <div class="bubble" style="left:643px;top:169px"><span>Flyer</span><span>500</span></div>
  <div class="bubble" style="left:685px;top:169px"><span>Poster</span><span>15</span></div>
  <div class="bubble" style="left:726px;top:169px"><span>Personen</span><span>1200–2500</span></div>

  <div class="card reisen"></div>
  <div class="abs txt" style="left:440px;top:229px;width:218px">
    <p><span class="head block-h">Reisen |</span> In Kooperation mit unseren Reisepartnern Sonnenweit und Reisehaus Nordlicht veranstaltet die JKI Reisen ins Ausland in Verbindung mit Fußballcamps. Professionelle Mitarbeiter, Trainer und Betreuer der Lindenhof Jugend Kick Institut (LJKI) sind bei den Camps vor Ort.</p>
    <p class="b" style="margin-top:3px">Tendenz 2016:</p>
    <ul class="dots"><li>8 Camps</li><li>25 – 30 Teilnehmer pro Reise</li><li>Türkei, Mallorca, Deutschland, uvm.</li></ul>
    <p class="b" style="margin-top:2px">Akquise von Teilnehmern:</p>
  </div>
  <div class="bubble" style="left:439px;top:325px"><span>Kataloge</span><span>150.000</span></div>
  <div class="bubble" style="left:481px;top:325px"><span>Messen</span><span>2 – 3</span></div>
  <div class="bubble" style="left:522px;top:325px"><span>Camps</span><span>30 – 40</span></div>
  <div class="bubble" style="left:563px;top:325px"><span>Flyer</span><span>ca. 5.000</span></div>
  <div class="brand" style="left:610px;top:296px;width:44px;font-size:7.5px;line-height:8.5px;text-align:center;white-space:normal">Reisehaus Nordlicht</div>
  <div class="brand" style="left:609px;top:336px;font-size:7.5px">Sonnenweit</div>
  <div class="photo" role="img" aria-label="Foto: Reisegruppe in grünen Trikots am Strand" style="left:663px;top:222px;width:112px;height:76px;transform:rotate(1.5deg);background:linear-gradient(180deg,#9ec7e6,#5f90b8 35%,#c9b893 60%,#5c9a3c)"></div>
  <div class="photo" role="img" aria-label="Foto: Fallrückzieher am Sandstrand vor Bergkulisse" style="left:675px;top:290px;width:104px;height:78px;transform:rotate(4deg);background:linear-gradient(180deg,#a7cbe8,#8fb0c8 40%,#d8c8a4 65%,#c7b38a)"></div>

  <div class="card schule"></div>
  <div class="photo" role="img" aria-label="Foto: Kind beim Hürdenlauf auf dem Sportplatz" style="left:440px;top:376px;width:92px;height:66px;transform:rotate(-3deg);background:linear-gradient(170deg,#6a9a45,#8dbb5e 55%,#4f7d31)"></div>
  <div class="photo" role="img" aria-label="Foto: Kinder beim gemeinsamen Essen" style="left:420px;top:436px;width:110px;height:76px;transform:rotate(4deg);background:linear-gradient(140deg,#c9a27e,#e6d2b2 50%,#8d6b4c)"></div>
  <div class="abs txt" style="left:548px;top:386px;width:215px">
    <p><span class="head block-h">Schulkooperationen |</span> Die LJBI bietet Schulen kostenfreie und ganzheitliche Konzepte sowie umfangreiche, sportartübergreifende und sportartspezifische Angebote in folgenden Bereichen an:</p>
    <ul class="dots" style="margin-top:2px"><li>Schulsport-Arbeitsgemeinschaften (AGs)</li><li>Schulsporttage</li><li>Schulturniere und -veranstaltungen</li><li>Gesundheit, Prävention und Ernährung</li></ul>
    <p style="margin-top:2px"><span class="b">Sporttage 2015:</span> 10 – 15<br><span class="b">Tendenz 2016:</span> &nbsp;&nbsp;&nbsp;40 – 60</p>
    <p class="b" style="margin-top:2px">So wurden 2015 etwa 400 – 600 Kinder für eine aktive Lebensweise begeistert.</p>
  </div>

  <!-- RIGHT PANEL -->
  <h1 class="panel-title" style="left:838px;top:42px">Sponsoringmöglichkeiten bei der LJBI</h1>

  <svg class="abs" style="left:800px;top:0" width="400" height="260" aria-label="Sponsorenpyramide" role="img">
    <g transform="translate(-800,0)">
      <polygon points="947,89 1024,238 870,238" fill="var(--white)" opacity=".85"/>
      <polygon points="947,94 953.5,116 940.5,116" fill="var(--navy)"/>
      <polygon points="953.9,118 965.7,140 928.3,140 940.1,118" fill="var(--magenta)"/>
      <polygon points="966.1,142 978,163 916,163 927.9,142" fill="var(--red)"/>
      <polygon points="978.4,165 990.2,187 903.8,187 915.6,165" fill="var(--orange)"/>
      <polygon points="990.6,189 1002.3,211 891.7,211 903.4,189" fill="var(--yellow)"/>
      <polygon points="1002.8,213 1019.5,236 874.5,236 891.2,213" fill="var(--green)"/>
      <g stroke="var(--white)" stroke-width="1.2">
        <line x1="958" y1="105" x2="1040" y2="105"/>
        <line x1="970" y1="129" x2="1040" y2="129"/>
        <line x1="983" y1="152" x2="1040" y2="152"/>
        <line x1="995" y1="176" x2="1040" y2="176"/>
        <line x1="1007" y1="200" x2="1040" y2="200"/>
        <line x1="1020" y1="224" x2="1040" y2="224"/>
      </g>
    </g>
  </svg>
  <span class="pyr-label" style="top:97px">Hauptsponsor</span>
  <span class="pyr-label" style="top:121px">Premium-Partner</span>
  <span class="pyr-label" style="top:144px">Top-Partner</span>
  <span class="pyr-label" style="top:168px">Partner</span>
  <span class="pyr-label" style="top:192px">Unterstützer</span>
  <span class="pyr-label" style="top:216px">Förderer</span>

  <div class="rule" style="top:257px"></div>

  <div class="tab" style="left:838px;top:280px;padding-right:18px">Camps</div>
  <div class="tab" style="left:838px;top:313px;padding-right:15px">Messen</div>
  <div class="tab" style="left:838px;top:346px;padding-right:17px">Reisen</div>
  <div class="csr">CSR</div>
  <div class="tab" style="left:952px;top:346px;font-size:9.5px;padding-right:14px">Spezial-<br>training</div>
  <div class="tab" style="left:1064px;top:280px;padding-right:16px">Events</div>
  <div class="tab" style="left:1064px;top:313px;padding-right:8px">Schultage</div>
  <div class="tab" style="left:1064px;top:346px;padding-right:2px">Soccercourt</div>

  <div class="rule" style="top:389px"></div>

  <div class="media" style="left:838px">
    <svg class="media-icon" viewBox="0 0 38 36" aria-hidden="true"><polygon points="1,1 37,1 37,24 19,35 1,24" fill="var(--blue)" stroke="var(--white)" stroke-width="1.5"/><rect x="10" y="7" width="18" height="11" fill="var(--white)"/><line x1="19" y1="18" x2="19" y2="26" stroke="var(--white)" stroke-width="1.5"/></svg>
    <h4>WERBEBANNER</h4><p>Beachflags<br>Beachbanner<br>Bandenwerbung<br>Sponsorenwand</p>
  </div>
  <div class="media" style="left:922px">
    <svg class="media-icon" viewBox="0 0 38 36" aria-hidden="true"><polygon points="1,1 37,1 37,24 19,35 1,24" fill="var(--blue)" stroke="var(--white)" stroke-width="1.5"/><g fill="none" stroke="var(--white)" stroke-width="1.2"><circle cx="19" cy="15" r="9"/><ellipse cx="19" cy="15" rx="4" ry="9"/><line x1="10" y1="15" x2="28" y2="15"/><line x1="11" y1="10.5" x2="27" y2="10.5"/><line x1="11" y1="19.5" x2="27" y2="19.5"/></g></svg>
    <h4>NEUE MEDIEN</h4><p>Homepagebanner<br>Sponsorenpyramide<br>Social-Media-Werbung</p>
  </div>
  <div class="media" style="left:1007px">
    <svg class="media-icon" viewBox="0 0 38 36" aria-hidden="true"><polygon points="1,1 37,1 37,24 19,35 1,24" fill="var(--blue)" stroke="var(--white)" stroke-width="1.5"/><path d="M14 6 L10 8 L7 13 L11 15 L12 13 L12 25 L26 25 L26 13 L27 15 L31 13 L28 8 L24 6 Q19 9 14 6Z" fill="var(--white)"/></svg>
    <h4>AUSRÜSTUNG</h4><p>Trikots<br>Hosen<br>Bälle<br>Trinkflaschen</p>
  </div>
  <div class="media" style="left:1092px">
    <svg class="media-icon" viewBox="0 0 38 36" aria-hidden="true"><polygon points="1,1 37,1 37,24 19,35 1,24" fill="var(--blue)" stroke="var(--white)" stroke-width="1.5"/><rect x="9" y="5" width="20" height="20" fill="var(--white)"/><g stroke="var(--blue)" stroke-width="1.2"><line x1="11" y1="9" x2="27" y2="9"/><line x1="11" y1="13" x2="18" y2="13"/><line x1="11" y1="17" x2="18" y2="17"/><line x1="11" y1="21" x2="27" y2="21"/></g><rect x="20" y="12" width="7" height="6" fill="var(--blue)"/></svg>
    <h4>PRINTMEDIEN</h4><p>Poster<br>Flyer<br>Werbeanzeigen<br>Infomaterial</p>
  </div>

</div>
</body>
</html>
```